Agriculture Business Card

I want to use my existing logo and use my tagline of "KNOW YOUR GROUND...TEST IT" on the card. Looking for a double sided card that will really get peoples attention.
Contact Info:
Marlow Field Crop Partners
Calvin Brusk
2716 K Lane
Brenfield, IA 50592
402-555-0143
calvin.r.brusk@fieldmailbox.net

```html
<!DOCTYPE html>
<html lang="en">
<head>
<meta charset="utf-8">
<title>Marlow Field Crop Partners – Business Card</title>
<link rel="stylesheet" href="https://fonts.googleapis.com/css2?family=Open+Sans:wght@400;700&family=Fira+Sans+Condensed:wght@600&display=swap">
<style>
  :root {
    --backdrop: #dcdcdc;
    --card-dark: #5a5a5a;
    --card-yellow: #ffec00;
    --earth-brown: #9a5b3d;
    --leaf-green: #4cbb3f;
    --harvest-orange: #fbb316;
  }
  * { margin: 0; padding: 0; box-sizing: border-box; }
  html, body {
    width: 1200px;
    height: 1105px;
    overflow: hidden;
    background: var(--backdrop);
  }
  .canvas {
    position: relative;
    width: 1200px;
    height: 1105px;
  }
  .card {
    position: absolute;
    top: 197px;
    width: 402px;
    height: 703px;
    border-radius: 22px;
  }
  .card-front {
    left: 170px;
    background: var(--card-dark);
  }
  .card-back {
    left: 628px;
    background: var(--card-yellow);
    color: var(--earth-brown);
    font-family: "Open Sans", sans-serif;
  }
  .brand-mark {
    position: absolute;
    top: 240px;
    left: 141px;
    width: 120px;
    height: 120px;
    border-radius: 50%;
    background: var(--harvest-orange);
  }
  .brand-name {
    position: absolute;
    top: 436px;
    left: 0;
    right: 0;
    font-family: "Fira Sans Condensed", sans-serif;
    font-weight: 600;
    font-size: 40px;
    line-height: 47px;
    letter-spacing: -0.5px;
    color: var(--earth-brown);
    text-align: center;
  }
  .holder-name {
    position: absolute;
    top: 54px;
    right: 52px;
    font-size: 24px;
    line-height: 32px;
    font-weight: 400;
  }
  .holder-name strong { font-weight: 700; }
  .contact {
    position: absolute;
    top: 438px;
    right: 46px;
    text-align: right;
    font-style: normal;
    font-size: 24px;
    line-height: 35px;
  }
  .contact .email { font-size: 21px; }
  .tagline {
    position: absolute;
    top: 620px;
    left: 17px;
    right: 46px;
    display: flex;
    align-items: center;
    gap: 10px;
  }
  .tagline-rule {
    width: 76px;
    height: 2px;
    background: var(--earth-brown);
  }
  .tagline-text {
    margin-left: auto;
    font-family: "Fira Sans Condensed", sans-serif;
    font-weight: 600;
    font-size: 22px;
    color: var(--leaf-green);
    white-space: nowrap;
  }
</style>
</head>
<body>
<main class="canvas">
  <section class="card card-front" aria-label="Card front">
    <div class="brand-mark"></div>
    <p class="brand-name">Marlow Field Crop<br>Partners</p>
  </section>

  <section class="card card-back" aria-label="Card back">
    <p class="holder-name">Calvin <strong>BRUSK</strong></p>
    <address class="contact">
      <div>402-555-0143</div>
      <div>2716 K Lane</div>
      <div>Brenfield, IA 50592</div>
      <div class="email">calvin.r.brusk@fieldmailbox.net</div>
    </address>
    <div class="tagline">
      <span class="tagline-rule"></span>
      <span class="tagline-text">KNOW YOUR GROUND...TEST IT</span>
    </div>
  </section>
</main>
</body>
</html>
```